Geothermal company needs a creative "POW" business card

Manufacturers tend to be boring. We are not! We are a Geothermal Heat Pump company that has over 30 yrs of experience and wants a new look and updated feel. Nothing old (yawn) so get your creative hats on and let's rock!

We want to use the great colors of lime green and navy blue. Our new logo is attached and we're ready to roll. Remember, we're a professional leader in the geothermal industry that needs to make an eye catching and memorable first glance.

```html
<!DOCTYPE html>
<html lang="en">
<head>
<meta charset="utf-8">
<title>Boreal Thermal Business Card</title>
<link href="https://fonts.googleapis.com/css2?family=Signika:wght@300;400;600&family=Roboto+Condensed:wght@400&display=swap" rel="stylesheet">
<style>
  :root {
    --navy: #00295b;
    --lime: #8dc63f;
    --green: #1d6b32;
    --paper: #ffffff;
    --stage: #efefef;
  }
  html, body {
    margin: 0;
    padding: 0;
    width: 1200px;
    height: 1000px;
    overflow: hidden;
    background: var(--stage);
    font-family: "Signika", sans-serif;
  }
  .canvas { position: relative; width: 1200px; height: 1000px; }
  .card {
    position: absolute;
    top: 355px;
    width: 496px;
    height: 280px;
    box-shadow: 0 10px 30px rgba(0,0,0,0.14);
    overflow: hidden;
  }
  .card--front {
    left: 67px;
    background: var(--paper);
    border-radius: 30px 0 30px 0;
  }
  .card--back {
    left: 639px;
    background: var(--navy);
    border-radius: 0 30px 0 30px;
  }
  .brand { position: absolute; display: flex; align-items: center; }
  .brand__mark { border-radius: 50%; flex: none; }
  .brand__name {
    font-weight: 600;
    color: var(--lime);
    line-height: 1;
    letter-spacing: -0.6px;
    white-space: nowrap;
  }
  .brand__tagline {
    font-family: "Roboto Condensed", sans-serif;
    line-height: 1;
    margin-top: 3px;
    white-space: nowrap;
  }
  .card--front .brand { left: 23px; top: 25px; }
  .card--front .brand__mark { width: 67px; height: 67px; background: var(--navy); margin-right: 17px; }
  .card--front .brand__name { font-size: 37px; }
  .card--front .brand__tagline { font-size: 10.5px; color: var(--navy); }
  .card--back .brand { left: 51px; top: 77px; }
  .card--back .brand__mark { width: 83px; height: 83px; background: var(--paper); margin-right: 20px; }
  .card--back .brand__name { font-size: 44px; }
  .card--back .brand__tagline { font-size: 13px; color: var(--paper); }
  .person { position: absolute; left: 29px; top: 124px; }
  .person__name { font-size: 21px; font-weight: 600; color: var(--navy); line-height: 1.2; }
  .person__title { font-size: 20px; font-weight: 300; color: var(--green); line-height: 1.3; }
  .contact {
    position: absolute;
    top: 199px;
    font-size: 16px;
    font-weight: 300;
    color: var(--lime);
    line-height: 21.5px;
    margin: 0;
  }
  .contact--lines { left: 29px; }
  .contact--address { right: 29px; text-align: right; font-style: normal; }
  .website {
    position: absolute;
    left: 0; right: 0;
    top: 208px;
    text-align: center;
    font-size: 25px;
    font-weight: 300;
    color: var(--paper);
    letter-spacing: 0.3px;
  }
</style>
</head>
<body>
<main class="canvas">
  <section class="card card--front">
    <div class="brand">
      <span class="brand__mark"></span>
      <div>
        <div class="brand__name">Boreal Thermal</div>
        <div class="brand__tagline">Builder of Ground Source Heat Systems for Cold Climates</div>
      </div>
    </div>
    <div class="person">
      <div class="person__name">Wes Lindqvist</div>
      <div class="person__title">CEO</div>
    </div>
    <p class="contact contact--lines">
      p: (555) 014-2200<br>
      f: (555) 014-2201<br>
      e: weslindqvist@borealthermal.com
    </p>
    <address class="contact contact--address">
      42 N Aspen Rd<br>
      Pinecrest, MN 55990
    </address>
  </section>

  <section class="card card--back">
    <div class="brand">
      <span class="brand__mark"></span>
      <div>
        <div class="brand__name">Boreal Thermal</div>
        <div class="brand__tagline">Builder of Ground Source Heat Systems for Cold Climates</div>
      </div>
    </div>
    <div class="website">www.borealthermal.com</div>
  </section>
</main>
</body>
</html>
```